Brochure Design Project

We sell and install rollout shelves for existing kitchen and bathroom cabinets. These rollout shelves are made of wood with dovetail joints. We also organize cabinets with pullouts, lazy susans, trash can pullouts, drawer organizers, and offer a selection of cabinet handles and knobs that we can also install.

Need extra days to review

```html
<!DOCTYPE html>
<html lang="en">
<head>
<meta charset="utf-8">
<title>Rollwell Brochure</title>
<link href="https://fonts.googleapis.com/css2?family=Lato:wght@400;700;900&display=swap" rel="stylesheet">
<style>
:root{
  --teal:#3fc8a8;
  --teal-deep:#2aa58c;
  --ink:#262729;
  --charcoal:#2d2e30;
  --slate:#3b5478;
  --grey-band:#9aa4a8;
  --paper:#ffffff;
  --text:#3a3a3a;
  --muted:#8b8f93;
}
*{margin:0;padding:0;box-sizing:border-box}
html,body{width:857px;height:1200px;overflow:hidden;background:var(--paper)}
body{font-family:'Lato',sans-serif;color:var(--text)}
.sheet{position:absolute;left:0;top:0;width:1000px;height:1400px;transform:scale(.857);transform-origin:0 0}
.box{position:absolute}
.photo{position:absolute}
p{line-height:1.28}

/* outer spread */
.welcome-panel{left:0;top:0;width:340px;height:385px;background:var(--charcoal)}
.welcome-panel h2{position:absolute;left:48px;top:46px;font-weight:400;font-size:21px;line-height:1.25;color:#d9d9d9}
.welcome-panel p{position:absolute;left:45px;top:122px;width:255px;font-size:10.5px;color:#cfcfcf}
.teal-panel{left:340px;top:0;width:325px;height:692px;background:var(--teal)}
.white-gap{left:340px;top:175px;width:325px;height:340px;background:var(--paper)}
.mini-feature{left:420px;top:640px;font-size:13px;color:#fff;line-height:1.15}
.mini-feature b{display:block}

.why{left:675px;top:18px;width:305px;height:285px}
.why h3{position:absolute;left:68px;top:30px;font-weight:400;font-size:16px;color:#fff;letter-spacing:.5px}
.why ul{position:absolute;left:38px;top:68px;list-style:none;width:250px}
.why li{display:flex;gap:10px;margin-bottom:12px;font-size:10px;color:#eee;line-height:1.3}
.why li svg{flex:none;margin-top:2px}
.bar{position:absolute;height:6px;background:var(--teal)}

.feature{left:708px;width:258px}
.feature .head{display:flex;align-items:center;gap:14px;margin-left:2px}
.feature .title{font-size:15px;line-height:1.2;color:#444}
.feature .title b{display:block;font-weight:900;color:#333}
.feature p{font-size:10.3px;margin-top:8px;color:#333}

/* inner spread */
.rail{top:705px;height:695px;background:var(--grey-band)}
.brand{left:53px;top:752px;width:255px;height:96px;background:var(--slate)}
.brand .name{position:absolute;left:56px;top:27px;font-weight:900;font-size:16px;color:#fff;letter-spacing:.5px}
.brand .tag{position:absolute;left:56px;top:46px;font-size:8.5px;color:#dfe6ee;letter-spacing:1px}
.brand .mark{position:absolute;left:18px;top:30px;width:22px;height:22px;background:var(--teal)}
.promise{left:53px;top:848px;width:255px;height:107px;background:var(--teal)}
.promise h2{position:absolute;left:24px;top:18px;font-weight:400;font-size:20px;line-height:1.23;color:#fff}
.friendly{left:75px;top:1200px;font-weight:700;font-size:18px;line-height:1.3;color:#2b2b2b;letter-spacing:.3px}
.friendly span{color:var(--teal)}

.hall-caption{left:343px;top:875px;width:657px;height:170px;background:linear-gradient(rgba(63,200,168,.15),rgba(30,150,130,.55))}
.col{position:absolute;top:925px;width:235px;color:#fff}
.col h4{font-weight:400;font-size:19px;margin-bottom:6px}
.col p{font-size:10.5px}

.contact{left:343px;top:1058px;width:324px;height:342px;background:var(--ink)}
.contact .label{position:absolute;left:33px;top:30px;width:135px;height:36px;background:#3a3b3d;color:#e3e3e3;font-size:16px;padding:9px 0 0 13px}
.contact .row{position:absolute;left:33px;font-size:10.5px;color:var(--muted);line-height:1.35}
.about-tag{left:703px;top:1081px;width:145px;height:38px;background:var(--charcoal);clip-path:polygon(0 0,88% 0,100% 100%,0 100%);color:#f2f2f2;font-size:16px;padding:10px 0 0 23px;letter-spacing:.5px}
.about{left:703px;top:1137px;width:257px;font-size:10.6px;color:#222}
</style>
</head>
<body>
<div class="sheet">

  <!-- outer spread -->
  <section class="box welcome-panel">
    <h2>Welcome to<br>Our Company...</h2>
    <p>Lorem ipsum dolor sit amet, consectetur adipisice elit, sed do eiusmod tempor incididunt ut labor et dolore magna aliqua. Ut enim ad minim venia quis nostrud exercitation ullamco laboris nisi ut aliquip ex ea commodo consequat. Duis aute ir reprehenderit in voluptate velit esse cillum dolore eu fu pariatur. Excepteur sint occaecat cupidatat non proid sunt in culpa qui officia deserunt mollit anim i laborum. Sed ut perspiciatis unde omnis iste ar voluptatem accusantium doloremque laudantium, to aperiam, eaque ipsa quae ab illo inventore verita architecto beatae vitae dicta sunt explicabo. Nemo en ipsam voluptatem quia voluptas sit.</p>
  </section>
  <div class="photo" role="img" aria-label="Open wooden drawer with utensil organizer dividers" style="left:0;top:385px;width:340px;height:310px;background:linear-gradient(135deg,#5a4028,#a07a48 45%,#6b4b2c)"></div>

  <div class="box teal-panel"></div>
  <div class="box white-gap"></div>
  <div class="photo" role="img" aria-label="Kitchen with wooden cabinets and granite countertop" style="left:376px;top:82px;width:256px;height:530px;background:linear-gradient(180deg,#6a3a1e,#9a5a2c 35%,#b49a78 60%,#4b3020)"></div>
  <div class="box mini-feature">Creative<b>Marketing</b></div>

  <div class="photo why" role="img" aria-label="Modern grey kitchen with white countertops" style="background:linear-gradient(135deg,#2f3436,#5c6466 55%,#8b9294)">
    <h3>WHY CHOOSE US?</h3>
    <ul>
      <li><svg width="16" height="16" viewBox="0 0 16 16"><circle cx="8" cy="8" r="7" fill="none" stroke="#3fc8a8" stroke-width="1.5"/><path d="M4.5 8.2l2.3 2.3 4.5-4.6" fill="none" stroke="#3fc8a8" stroke-width="1.6"/></svg>Lorem ipsum dolor sit amet, cons adipisicing elit, sed do eiusmod tempor.</li>
      <li><svg width="16" height="16" viewBox="0 0 16 16"><circle cx="8" cy="8" r="7" fill="none" stroke="#3fc8a8" stroke-width="1.5"/><path d="M4.5 8.2l2.3 2.3 4.5-4.6" fill="none" stroke="#3fc8a8" stroke-width="1.6"/></svg>Lorem ipsum dolor sit amet, cons adipisicing elit, sed do eiusmod tempor.</li>
      <li><svg width="16" height="16" viewBox="0 0 16 16"><circle cx="8" cy="8" r="7" fill="none" stroke="#3fc8a8" stroke-width="1.5"/><path d="M4.5 8.2l2.3 2.3 4.5-4.6" fill="none" stroke="#3fc8a8" stroke-width="1.6"/></svg>Lorem ipsum dolor sit amet, cons adipisicing elit, sed do eiusmod tempor.</li>
      <li><svg width="16" height="16" viewBox="0 0 16 16"><circle cx="8" cy="8" r="7" fill="none" stroke="#3fc8a8" stroke-width="1.5"/><path d="M4.5 8.2l2.3 2.3 4.5-4.6" fill="none" stroke="#3fc8a8" stroke-width="1.6"/></svg>Lorem ipsum dolor sit amet, cons adipisicing elit, sed do eiusmod tempor.</li>
    </ul>
    <div class="bar" style="left:43px;top:234px;width:162px"></div>
    <div class="bar" style="left:75px;top:250px;width:135px"></div>
  </div>

  <article class="box feature" style="top:316px">
    <div class="head">
      <svg width="42" height="42" viewBox="0 0 42 42"><polygon points="21,2 37,11 37,31 21,40 5,31 5,11" fill="none" stroke="#9fb7c9" stroke-dasharray="2 2"/><path d="M13 18h4l8-5v16l-8-5h-4z M17 24l2 5" fill="none" stroke="#2d2e30" stroke-width="1.8"/></svg>
      <div class="title">Creative<b>Marketing</b></div>
    </div>
    <p>Lorem ipsum dolor sit amet, conse adipisicing elit, sed do eiusmod tempor incididunt laboreli dolore magna aliquat enim ad minim.</p>
  </article>
  <article class="box feature" style="top:430px">
    <div class="head">
      <svg width="42" height="42" viewBox="0 0 42 42"><polygon points="21,2 37,11 37,31 21,40 5,31 5,11" fill="none" stroke="#9fb7c9" stroke-dasharray="2 2"/><path d="M11 21l19-8-6 17-4-6z M20 24l10-11" fill="none" stroke="#2d2e30" stroke-width="1.8"/></svg>
      <div class="title">Creative<b>Branding</b></div>
    </div>
    <p>Lorem ipsum dolor sit amet, conse adipisicing elit, sed do eiusmod tempor incididunt laboreli dolore magna aliquat enim ad minim.</p>
  </article>
  <article class="box feature" style="top:544px">
    <div class="head">
      <svg width="42" height="42" viewBox="0 0 42 42"><polygon points="21,2 37,11 37,31 21,40 5,31 5,11" fill="none" stroke="#9fb7c9" stroke-dasharray="2 2"/><path d="M21 11a6 6 0 0 1 4 10.5v3h-8v-3A6 6 0 0 1 21 11z M18 28h6" fill="none" stroke="#2d2e30" stroke-width="1.8"/></svg>
      <div class="title">Creative<b>Solution</b></div>
    </div>
    <p>Lorem ipsum dolor sit amet, conse adipisicing elit, sed do eiusmod tempor incididunt laboreli dolore magna aliquat enim ad minim.</p>
  </article>

  <!-- inner spread -->
  <div class="box rail" style="left:0;width:53px"></div>
  <div class="box rail" style="left:308px;width:35px"></div>

  <header class="box brand">
    <div class="mark"></div>
    <div class="name">ROLLWELL</div>
    <div class="tag">TAGLINE HERE</div>
  </header>
  <div class="box promise"><h2>We Will<br>Give Your Best<br>Business Services</h2></div>
  <div class="photo" role="img" aria-label="Dark cabinet interior" style="left:53px;top:955px;width:255px;height:130px;background:linear-gradient(180deg,#2b2f36,#1a1c20)"></div>
  <div class="bar" style="left:77px;top:1092px;width:207px;height:8px;background:linear-gradient(90deg,var(--teal) 33%,#5fd0c0 33% 66%,var(--teal-deep) 66%)"></div>
  <div class="photo" role="img" aria-label="Wooden rollout shelves under a kitchen sink cabinet" style="left:53px;top:1105px;width:255px;height:240px;background:linear-gradient(180deg,#6b2a1c,#b88a5a 50%,#d8c9a8)"></div>
  <div class="box friendly"><span>WE ARE<br>ALWAYS<br>IN</span><br>FRIENDLY<br>COMMUNICATION</div>

  <div class="photo" role="img" aria-label="Bright multi-storey showroom hall with information desk" style="left:343px;top:705px;width:657px;height:340px;background:linear-gradient(180deg,#1f2c45,#6d7a8c 45%,#3a6a78)"></div>
  <div class="box hall-caption"></div>
  <div class="col" style="left:377px"><h4>Text</h4><p>Lorem ipsum dolor sit amet, consectetuadip-isicing elit, sed do eiusmod tempor incididunt ut labore et dolore magna aliqua. U enim ad minim veniam, quis nostrud exercitation ulla-mco laboris nisi ut aliquip ex ea cconsequat.</p></div>
  <div class="col" style="left:702px"><h4>Text</h4><p>Lorem ipsum dolor sit amet, consectetuadip-isicing elit, sed do eiusmod tempor incididunt ut labore et dolore magna aliqua. U enim ad minim veniam, quis nostrud exercitation ulla-mco laboris nisi ut aliquip ex ea cconsequat.</p></div>

  <section class="box contact">
    <div class="label">Contact Us</div>
    <svg style="position:absolute;left:33px;top:88px" width="24" height="20" viewBox="0 0 24 20"><path d="M3 6c0-3 18-3 18 0v2h-4V6H7v2H3z M6 9h12l2 9H4z" fill="none" stroke="#8b8f93" stroke-width="1.5"/><circle cx="12" cy="13.5" r="2.5" fill="none" stroke="#8b8f93" stroke-width="1.5"/></svg>
    <div class="row" style="top:116px">Pho : 555-204-7781<br>Tel : 555-204-7781</div>
    <svg style="position:absolute;left:33px;top:162px" width="22" height="22" viewBox="0 0 22 22" fill="none" stroke="#8b8f93" stroke-width="1.4"><circle cx="11" cy="11" r="9.5"/><ellipse cx="11" cy="11" rx="4" ry="9.5"/><path d="M1.5 11h19M3 6h16M3 16h16"/></svg>
    <div class="row" style="top:188px">Email : hello@rollwellshelves.com<br>Web : www.rollwellshelves.com</div>
    <svg style="position:absolute;left:34px;top:237px" width="16" height="22" viewBox="0 0 16 22"><path d="M8 1a7 7 0 0 1 7 7c0 5-7 13-7 13S1 13 1 8a7 7 0 0 1 7-7z" fill="none" stroke="#8b8f93" stroke-width="1.5"/><circle cx="8" cy="8" r="2.5" fill="#8b8f93"/></svg>
    <div class="row" style="top:262px">Add : 48 Cedar Grove Lane<br>Maple Falls, OR 97000</div>
  </section>

  <div class="box about-tag">ABOUT US</div>
  <p class="box about">Lorem ipsum dolor sit amet, consectetur adipisice elit, sed do eiusmod tempor incididunt ut labor et dolore magna aliqua. Ut enim ad minim venia quis nostrud exercitation ullamco laboris nisi ut aliquip elcommodo consequat. Duis aute ir reprehenderit in voluptate velit esse cillum dolore eu fu pariatur. Excepteur sint occaecat cupidatat non proid sunt in culpa qui officia deserunt mollit anim i laborum. Sed ut perspiciatis unde omnis iste ar voluptatem accusantium doloremque laudantium, to aperiam, eaque ipsa quae ab illo inventore verita architecto beatae vitae dicta sunt explicabo. Nemo en ipsam voluptatem quia voluptas sit aspernatur aut odil fugit, sed quia consequuntur magni dolores eo qui ratione voluptatem sequi nesciunt.</p>

</div>
</body>
</html>
```